Website for cardiology consultation and diagnostics in Canada

Hi there, thank you for considering to take on this project.

Our Cardiology would like designs for a website. we are a cardiology group comprised of 7 doctors. We need a functioning site.

Key design themes should highlight simplicity and serenity. Website shouldnt be complicated or crowded. Less words and more graphics. It should be mobile friendly. The winning submission should work with us for revisions until we get it right.

Sections:
Front page - who we are, why choose us. (1 - 2 paragraphs, Lorem Ipsum)

1. Requisition form (can download our latest requisition form, and create the same form online for submission as well)
2. Services provided: EKG, Echo, Stress Echo, Holter, Loop, Ambulatory BP monitors. One or two paragraphs on each of these tests with graphics.
3. Our physicians: Dr A, B, C, D, E, F, G (short bio with random pix)
4. About us: A few paragraph about how we started (Lorem Ipsum)
5. Location : design a simple page for our Address and location (map)
6. Contact us : design a page for feedback

We have included most of the material in other aspects of our practice including our color themes and logos

Current website is larkfieldpulse.org

Target Market(s)

Other physicians, patients

Industry/Entity Type

Health Care

Number of Pages Required

5+ page

Requirements
Must have
• Pages as described above
• Ability to do revisions later
• Pictures
• Simple and elegant
Should not have
• Too wordy or complicated designs

```html
<!DOCTYPE html>
<html lang="en">
<head>
<meta charset="utf-8">
<title>Larkfield Pulse Institute</title>
<link href="https://fonts.googleapis.com/css2?family=Cinzel:wght@400;600;700&family=Open+Sans:wght@400;600;700&display=swap" rel="stylesheet">
<style>
:root{
  --red:#c41f2a;
  --red-dark:#a8171f;
  --navy:#174a7c;
  --navy-deep:#0f3a66;
  --ink:#222;
  --text:#555;
  --light:#f1f3f5;
  --dark:#232323;
  --white:#fff;
}
*{box-sizing:border-box;margin:0;padding:0}
html,body{width:1200px;height:4196px;overflow:hidden}
body{font-family:"Open Sans",Arial,sans-serif;color:var(--text);background:var(--white);position:relative}
section,header,footer{position:relative;width:1200px}
.serif{font-family:"Cinzel",Georgia,serif}

/* header */
.site-header{height:84px;display:flex;align-items:center;justify-content:space-between;padding:0 67px 0 60px;background:var(--white)}
.brand{display:flex;align-items:center;gap:10px;font-weight:700;font-size:17px;color:var(--red)}
.brand-dot{width:18px;height:18px;border-radius:50%;background:var(--red)}
.main-nav{display:flex;gap:44px}
.main-nav a{font-size:13px;font-weight:600;color:var(--ink);text-decoration:none;text-transform:uppercase}

/* hero */
.hero{height:517px;text-align:center;color:var(--white)}
.hero-photo{position:absolute;inset:0;background:linear-gradient(180deg,#7c8f98 0%,#5f7884 45%,#4b6672 100%)}
.hero-content{position:relative;padding-top:180px}
.hero h1{font-size:50px;font-weight:600;letter-spacing:2px}
.hero p{font-size:15px;width:640px;margin:10px auto 0;line-height:1.55}
.btn-outline{display:inline-block;margin-top:36px;width:238px;height:50px;line-height:46px;border:2px solid var(--white);color:var(--white);font-weight:600;font-size:15px}
.hero-tab{position:absolute;left:498px;bottom:0;width:204px;height:44px;background:var(--red);color:var(--white);font-size:12px;line-height:48px;text-transform:uppercase}
.hero-tab-knob{position:absolute;left:589px;bottom:34px;width:22px;height:22px;border-radius:50%;background:var(--ink);border:2px solid var(--white)}

/* requisition */
.requisition{height:182px;background:var(--red);padding:36px 84px 0}
.requisition h2{font-size:36px;font-weight:600;color:var(--white);letter-spacing:1px}
.req-form{display:flex;gap:20px;margin-top:16px}
.field{height:42px;background:var(--white);font-size:12px;color:#999;padding:12px 12px;width:260px}
.btn-submit{width:173px;height:42px;margin-left:5px;background:var(--navy);color:var(--white);font-weight:700;font-size:14px;text-align:center;line-height:42px;text-transform:uppercase}

/* why */
.why{height:587px}
.why-text{position:absolute;left:58px;top:95px;width:420px}
.section-title{font-size:44px;font-weight:400;color:var(--ink);letter-spacing:2px}
.why-text p{font-size:13px;line-height:1.6;margin-top:14px}
.btn-red{display:inline-block;background:var(--red);color:var(--white);font-size:13px;font-weight:600;text-align:center}
.why .btn-red{position:absolute;left:62px;top:453px;width:162px;height:42px;line-height:42px}
.why-photo{position:absolute;left:490px;top:56px;width:670px;height:531px;background:radial-gradient(ellipse at 40% 55%,#cfe0ee 0%,#e8eef4 45%,#ffffff 78%)}

/* services */
.services{height:605px;background:var(--navy)}
.services .section-title{color:var(--white);position:absolute;left:60px;top:56px}
.service-card{position:absolute;top:149px;width:335px}
.service-photo{height:179px;border:3px solid #3c6a97;background:linear-gradient(135deg,#9fb6c8,#dfe6ec 55%,#8aa0b2)}
.service-card h3{color:var(--white);font-size:19px;font-weight:700;margin-top:22px}
.service-card p{color:#d8e3ee;font-size:13px;line-height:1.55;margin-top:6px}
.service-card .btn-red{margin-top:16px;width:106px;height:32px;line-height:32px;font-size:12px}
.slider-arrow{position:absolute;top:270px}

/* physicians */
.physicians{height:662px}
.physicians .section-title{position:absolute;left:58px;top:80px}
.phys-arrows{position:absolute;left:1049px;top:193px;display:flex;gap:15px}
.phys-arrow{width:27px;height:25px;background:var(--ink);display:flex;align-items:center;justify-content:center}
.phys-card{position:absolute;top:232px;width:255px}
.phys-photo{height:246px;background:linear-gradient(180deg,#e6eaee 0%,#d4dde5 60%,#f4f6f8 100%)}
.phys-caption{height:73px;background:#eeeeee;text-align:center;padding-top:16px}
.phys-caption h4{color:var(--navy);font-size:15px;font-weight:700}
.phys-caption span{font-size:12px;color:#777}

/* about */
.about{height:496px;background:linear-gradient(90deg,#ffffff 40%,#f1f4f7 100%)}
.about-photo{position:absolute;left:0;top:0;width:560px;height:496px;background:radial-gradient(ellipse at 30% 50%,#cdd9e3 0%,#e9eef2 55%,#ffffff 90%)}
.about-text{position:absolute;left:573px;top:90px;width:560px}
.about-text p{font-size:13px;line-height:1.65;margin-top:14px}
.about-text strong{color:var(--ink)}

/* location */
.location{height:553px;background:radial-gradient(ellipse at 60% 40%,#1f5a96 0%,var(--navy-deep) 70%)}
.pulse-line{position:absolute;left:0;top:0}
.map{position:absolute;left:62px;top:106px;width:483px;height:394px;background:#e7e7e4;border:6px solid var(--white)}
.loc-info{position:absolute;left:590px;top:120px;color:var(--white)}
.loc-info h3{font-size:25px;font-weight:600;letter-spacing:1px}
.loc-info h4{font-size:19px;font-weight:600;margin-top:30px;margin-left:8px}
.loc-item{display:flex;gap:16px;align-items:flex-start;margin-top:24px;margin-left:8px;font-size:14px;line-height:1.6}
.loc-icon{flex:0 0 26px;height:26px;border-radius:50%;background:#2c9fd9;display:flex;align-items:center;justify-content:center}

/* contact */
.contact{height:510px;background:var(--dark);text-align:center}
.contact .section-title{color:var(--white);padding-top:50px;font-size:50px}
.contact-form{position:absolute;left:274px;top:140px;width:671px}
.c-row{display:flex;justify-content:space-between;margin-bottom:20px}
.c-field{width:322px;height:42px;border:1px solid #555;color:#888;font-size:13px;text-align:left;padding:11px 12px}
.c-message{width:671px;height:95px;border:1px solid #555;color:#888;font-size:13px;text-align:left;padding:12px}
.contact .btn-red{position:absolute;left:509px;top:372px;width:224px;height:53px;line-height:53px;font-size:16px}
.footer-rule{position:absolute;left:370px;top:454px;width:460px;height:1px;background:#444}
.copyright{position:absolute;left:0;right:0;top:468px;font-size:13px;color:#aaa}
</style>
</head>
<body>

<header class="site-header">
  <div class="brand"><span class="brand-dot"></span>Larkfield Pulse</div>
  <nav class="main-nav">
    <a>Home</a><a>Services Provided</a><a>Our Physicians</a><a>About Us</a><a>Location</a><a>Contact Us</a>
  </nav>
</header>

<section class="hero">
  <div class="hero-photo" role="img" aria-label="Soft blurred clinic background in grey and teal tones"></div>
  <div class="hero-content">
    <h1 class="serif">LARKFIELD PULSE INSTITUTE</h1>
    <p>Lorem Ipsum has been the industry's standard dummy text ever since the 1500s and scrambled it to make a type specimen book.</p>
    <span class="btn-outline">Get Appointment</span>
  </div>
  <div class="hero-tab">Requisition Form</div>
  <div class="hero-tab-knob"></div>
</section>

<section class="requisition">
  <h2 class="serif">REQUISITION FORM</h2>
  <div class="req-form">
    <div class="field">Your Name</div>
    <div class="field">Your Email</div>
    <div class="field">Message</div>
    <div class="btn-submit">Submit</div>
  </div>
</section>

<section class="why">
  <div class="why-text">
    <h2 class="section-title serif">WHY CHOOSE US</h2>
    <p>Lorem Ipsum is simply dummy text of the printing and typesetting industry. Lorem Ipsum has been the industry's standard dummy text ever since the 1500s and scrambled it to make a type specimen book.</p>
    <p>It has survived not only five centuries, but also the leap into electronic typesetting, remaining essentially unchanged. It was popularised in the 1960s with the release of Letraset sheets containing Lorem Ipsum passages, and more recently with desktop publishing software like Aldus PageMaker including versions of Lorem Ipsum.</p>
  </div>
  <span class="btn-red">More Details</span>
  <div class="why-photo" role="img" aria-label="Smiling nurse drawing a heart in the air with a team of doctors behind her"></div>
</section>

<section class="services">
  <h2 class="section-title serif">SERVICE PROVIDED</h2>
  <svg class="slider-arrow" style="left:22px" width="16" height="26" viewBox="0 0 16 26"><path d="M13 2L3 13l10 11" fill="none" stroke="#fff" stroke-width="3"/></svg>
  <svg class="slider-arrow" style="left:1162px" width="16" height="26" viewBox="0 0 16 26"><path d="M3 2l10 11L3 24" fill="none" stroke="#fff" stroke-width="3"/></svg>
  <div class="service-card" style="left:56px">
    <div class="service-photo" role="img" aria-label="Technician running an EKG test on a patient"></div>
    <h3>EKG Services</h3>
    <p>Lorem Ipsum has been the industry's standard dummy text ever since the 1500s, when an unknown printer took a galley of type and scrambled it to make a type specimen book.</p>
    <span class="btn-red">View Details</span>
  </div>
  <div class="service-card" style="left:431px">
    <div class="service-photo" role="img" aria-label="Doctor reviewing echo results with a patient"></div>
    <h3>Echo Services</h3>
    <p>Lorem Ipsum has been the industry's standard dummy text ever since the 1500s, when an unknown printer took a galley of type and scrambled it to make a type specimen book.</p>
    <span class="btn-red">View Details</span>
  </div>
  <div class="service-card" style="left:806px">
    <div class="service-photo" role="img" aria-label="Patient undergoing a stress echo examination"></div>
    <h3>Stress Echo Services</h3>
    <p>Lorem Ipsum has been the industry's standard dummy text ever since the 1500s, when an unknown printer took a galley of type and scrambled it to make a type specimen book.</p>
    <span class="btn-red">View Details</span>
  </div>
</section>

<section class="physicians">
  <h2 class="section-title serif">OUR PHYSICIANS</h2>
  <div class="phys-arrows">
    <div class="phys-arrow"><svg width="8" height="12" viewBox="0 0 8 12"><path d="M7 1L2 6l5 5" fill="none" stroke="#fff" stroke-width="2"/></svg></div>
    <div class="phys-arrow"><svg width="8" height="12" viewBox="0 0 8 12"><path d="M1 1l5 5-5 5" fill="none" stroke="#fff" stroke-width="2"/></svg></div>
  </div>
  <div class="phys-card" style="left:67px">
    <div class="phys-photo" role="img" aria-label="Portrait of a physician in a white coat"></div>
    <div class="phys-caption"><h4>Dr. Aravind (Ravi) Mehta</h4><span>Neurosurgeon</span></div>
  </div>
  <div class="phys-card" style="left:333px">
    <div class="phys-photo" role="img" aria-label="Portrait of a physician in a white coat"></div>
    <div class="phys-caption"><h4>Dr. Simon Haddad</h4><span>Dentist</span></div>
  </div>
  <div class="phys-card" style="left:601px">
    <div class="phys-photo" role="img" aria-label="Portrait of a physician in a white coat"></div>
    <div class="phys-caption"><h4>Dr. Aravind (Ravi) Mehta</h4><span>Cardiologist</span></div>
  </div>
  <div class="phys-card" style="left:867px">
    <div class="phys-photo" role="img" aria-label="Portrait of a physician in a white coat"></div>
    <div class="phys-caption"><h4>Dr. Simon Haddad</h4><span>Gynecologist</span></div>
  </div>
</section>

<section class="about">
  <div class="about-photo" role="img" aria-label="Doctor holding a stethoscope toward the viewer"></div>
  <div class="about-text">
    <h2 class="section-title serif">ABOUT LPI</h2>
    <p>Almost daily medical device companies, doctors and surgeons all over the world develop new or breakthrough products, medical and surgical techniques. These techniques save lives or increase the survival rate of some patients.</p>
    <p>It is therefore very important that these medical device companies, doctors and surgeons share their knowledge as fast and accurate as possible. The current methods to share this knowledge are peer-to-peer live medical teachings and live medical teaching at conferences.</p>
    <p><strong>Peer-to-peer live medical teaching</strong><br>Healthcare companies contract top surgeons to do teaching sessions with their appliances/equipment.</p>
  </div>
</section>

<section class="location">
  <svg class="pulse-line" width="1200" height="553" viewBox="0 0 1200 553"><path d="M0 340H300l20-30 18 60 24-200 26 300 22-130h260l18-40 22 70 22-250 24 330 20-110H1200" fill="none" stroke="#3b78b4" stroke-width="2" opacity=".55"/></svg>
  <div class="map" role="img" aria-label="Street map showing the clinic location with a red pin"></div>
  <div class="loc-info">
    <h3 class="serif">LARKFIELD PULSE INSTITUTE</h3>
    <h4>We have moved from</h4>
    <div class="loc-item">
      <span class="loc-icon"><svg width="12" height="14" viewBox="0 0 12 14"><path d="M6 0a5 5 0 0 0-5 5c0 4 5 9 5 9s5-5 5-9a5 5 0 0 0-5-5zm0 7a2 2 0 1 1 0-4 2 2 0 0 1 0 4z" fill="#fff"/></svg></span>
      <span>412 Brookvale Avenue, Suite 101, Larkfield Ontario :<br>2810 Maplecrest Avenue, Suite 201<br>Larkfield ON L4K 2P7</span>
    </div>
    <div class="loc-item">
      <span class="loc-icon"><svg width="13" height="13" viewBox="0 0 13 13"><path d="M3 1l2 3-1.5 1.5a7 7 0 0 0 4 4L9 8l3 2-1.5 2.5C6 12 1 7 .5 2.5z" fill="#fff"/></svg></span>
      <span>Phone: 555-014-2286</span>
    </div>
    <div class="loc-item">
      <span class="loc-icon"><svg width="13" height="12" viewBox="0 0 13 12"><rect x="3" y="0" width="7" height="4" fill="#fff"/><rect x="0" y="4" width="13" height="5" fill="#fff"/><rect x="3" y="8" width="7" height="4" fill="#fff"/></svg></span>
      <span>Fax : 555-014-7731</span>
    </div>
    <div class="loc-item">
      <span class="loc-icon"><svg width="13" height="10" viewBox="0 0 13 10"><rect x="0" y="0" width="13" height="10" fill="#fff"/><path d="M0 0l6.5 5L13 0" fill="none" stroke="#2c9fd9" stroke-width="1.3"/></svg></span>
      <span>Email : contact@larkfieldpulse.org</span>
    </div>
  </div>
</section>

<footer class="contact">
  <h2 class="section-title serif">CONTACT US</h2>
  <div class="contact-form">
    <div class="c-row"><div class="c-field">Your Name</div><div class="c-field">City</div></div>
    <div class="c-row"><div class="c-field">Mobile</div><div class="c-field">Email</div></div>
    <div class="c-message">Your Message</div>
  </div>
  <span class="btn-red">Submit Request</span>
  <div class="footer-rule"></div>
  <p class="copyright">Copyright © 2017 Larkfield Pulse Institute. All Rights Reserved</p>
</footer>

</body>
</html>
```